Lottery Scratchcard templates for charities

We produce scratch cards for charities to sell to their supporters to raise funds.

We need a set of templates which can be re-used for different clients by simply replacing text, logo, prizes and a potentially a picture.

One of the templates can be plain simply using block colours
One can use generic images like a treasure chests which indicate money can be won
One templates can feature space for a photograph which can be easily replaced and updated depending on the client - example, a picture of a dog for a dog charity can easily be replaced by a picture of a football team for a club.

Target Market(s)

People who support a charity and the charities themselves

Industry/Entity Type

Charity

Colors

Designer to choose colors to be used in the design.

Requirements
Must have
• Every card will need space for:
• - The charity's logo
• - our logo
• - a panel which can be scratched off (use a plain silver, but can have an image printed on top in black only)
• - information about how to win (this can be lorem ipsum text)
• - Prizes (usually 4 or 5 prize levels of £100, £50, £10, £1)
• - Price: £1 and/or Just £1 to play
• - Small print - "Please play responsibly www.KeelbrookTrust.org."
• minimum size 4pt
• Paper size: A7, print ready
• Format: Adobe InDesign, fully editable
• Vector illustrations/design elements

```html
<!DOCTYPE html>
<html lang="en">
<head>
<meta charset="utf-8">
<title>Bingo Scratchcard – Nestwell</title>
<link href="https://fonts.googleapis.com/css2?family=Open+Sans:wght@400;600;700&family=Lobster&family=Bangers&family=Tinos&display=swap" rel="stylesheet">
<style>
  :root {
    --navy: #1d2a5c;
    --navy-light: #2c3f80;
    --white: #ffffff;
    --red: #e8262b;
    --purple: #7b3f98;
    --orange: #ef5a24;
    --green: #2e8b3e;
    --pink: #e0197d;
    --cyan: #1bb6e8;
    --panel-grey: #bcbcbc;
    --ink: #111111;
    --gold: #f5b81c;
    --wood: #8a5424;
  }
  * { margin: 0; padding: 0; box-sizing: border-box; }
  html, body { width: 850px; height: 1200px; overflow: hidden; background: var(--navy); }
  .card {
    position: relative;
    width: 850px; height: 1200px;
    overflow: hidden;
    background: radial-gradient(circle at 50% 45%, var(--navy-light) 0%, var(--navy) 65%);
    font-family: "Open Sans", Arial, sans-serif;
  }
  .logo-spot {
    position: absolute;
    width: 300px; height: 300px;
    border-radius: 50%;
    background: var(--white);
    display: flex; align-items: center; justify-content: center;
    text-align: center;
  }
  .logo-spot--charity { left: 75px; top: 55px; }
  .logo-spot--operator { left: 480px; top: 55px; }
  .charity-placeholder {
    font-family: "Tinos", "Times New Roman", serif;
    font-size: 22px; line-height: 30px; color: var(--ink);
  }
  .operator-name {
    font-weight: 700; font-size: 46px; color: var(--purple);
  }
  .treasure-art {
    position: absolute;
    left: 165px; top: 455px;
    width: 525px; height: 430px;
    border-radius: 40px 40px 120px 120px;
    background: radial-gradient(ellipse at 45% 40%, #ffd34d 0%, var(--gold) 40%, var(--wood) 85%, rgba(29,42,92,0) 100%);
  }
  .prize {
    position: absolute;
    font-family: "Lobster", cursive;
    line-height: 1;
    text-shadow: 3px 3px 0 var(--white), -3px -3px 0 var(--white), 3px -3px 0 var(--white), -3px 3px 0 var(--white), 7px 7px 0 var(--navy);
    transform: rotate(-6deg);
  }
  .prize--100 { left: 125px; top: 335px; font-size: 140px; color: var(--red); }
  .prize--50  { left: 540px; top: 378px; font-size: 100px; color: var(--purple); }
  .prize--10  { left: 95px;  top: 600px; font-size: 110px; color: var(--orange); }
  .prize--1   { left: 490px; top: 596px; font-size: 78px;  color: var(--green); }
  .bingo {
    position: absolute;
    left: 250px; top: 492px;
    font-family: "Bangers", cursive;
    font-size: 118px; line-height: 1;
    color: var(--red);
    transform: rotate(-12deg);
    text-shadow: 3px 3px 0 var(--white), -3px -3px 0 var(--white), 3px -3px 0 var(--white), -3px 3px 0 var(--white), 6px 6px 0 var(--navy);
  }
  .price-badge { position: absolute; left: 605px; top: 700px; width: 200px; height: 200px; }
  .how-to-win {
    position: absolute;
    left: 92px; top: 886px;
    width: 624px; height: 210px;
    background: var(--panel-grey);
    text-align: center;
    color: var(--ink);
  }
  .how-to-win__title { font-size: 38px; font-weight: 400; line-height: 1; margin-top: 16px; }
  .how-to-win__rules { font-size: 14px; line-height: 19px; margin-top: 4px; }
  .scratch-area {
    position: absolute;
    left: 30px; top: 105px;
    width: 570px; height: 87px;
    border: 3px solid var(--ink);
    display: flex; flex-direction: column; justify-content: center;
  }
  .scratch-area__rule { font-size: 16px; color: var(--red); }
  .scratch-area__tag { font-size: 25px; color: var(--purple); margin-top: 2px; }
  .cause {
    position: absolute; left: 0; top: 1116px; width: 850px;
    text-align: center; color: var(--white);
    font-weight: 700; font-size: 19px;
  }
  .small-print {
    position: absolute; left: 0; top: 1154px; width: 850px;
    text-align: center; color: var(--white);
    font-size: 13px;
  }
</style>
</head>
<body>
<main class="card">
  <div class="logo-spot logo-spot--charity">
    <p class="charity-placeholder">THE<br>CHARITY'S<br>LOGO</p>
  </div>
  <div class="logo-spot logo-spot--operator">
    <p class="operator-name">Nestwell</p>
  </div>

  <div class="treasure-art" role="img" aria-label="Illustration of an open treasure chest overflowing with gold coins, jewels and pearls"></div>

  <p class="prize prize--100">£100</p>
  <p class="prize prize--50">£50</p>
  <p class="bingo">BINGO!</p>
  <p class="prize prize--10">£10</p>
  <p class="prize prize--1">£1</p>

  <svg class="price-badge" viewBox="0 0 200 200" aria-label="Just £1 to play">
    <defs>
      <path id="badge-ring" d="M100,100 m-80,0 a80,80 0 1,1 160,0 a80,80 0 1,1 -160,0"/>
    </defs>
    <circle cx="100" cy="100" r="100" fill="var(--pink)"/>
    <text font-family="Open Sans, sans-serif" font-size="15" fill="#fff">
      <textPath href="#badge-ring" textLength="496" lengthAdjust="spacing">JUST £1 TO PLAY • JUST £1 TO PLAY •</textPath>
    </text>
    <text x="100" y="125" text-anchor="middle" font-family="Lobster, cursive" font-size="78" fill="var(--cyan)" stroke="#fff" stroke-width="2" transform="rotate(-8 100 100)">£1</text>
  </svg>

  <section class="how-to-win">
    <h2 class="how-to-win__title">HOW TO WIN</h2>
    <p class="how-to-win__rules">(THIS CAN BE LOREM IPSUM TEXT (THIS CAN BE LOREM IPSUM TEXT<br>(THIS CAN BE LOREM IPSUM TEXT (THIS CAN BE LOREM IPSUM TEXT</p>
    <div class="scratch-area">
      <p class="scratch-area__rule">MATCH 3 TO WIN THE AMOUNT SHOWN!</p>
      <p class="scratch-area__tag">SCRATCH &amp; SUPPORT</p>
    </div>
  </section>

  <p class="cause">All proceeds will help Nestwell support the health and wellbeing of local families.</p>
  <p class="small-print">Please play responsibly www.KeelbrookTrust.org</p>
</main>
</body>
</html>
```